7QK Pop Up Shop Clearance Flyer

We sell furniture. We opened up recently a temporary pop up shop to clear some stock we had from our old shop. So we don't have a full collection just our clearance lines that we want to get rid of - but the customer doesn't need to know this! Therefore the aim of this leaflet is to attract customers and make them come in - once they are there they might see something they like. As we will not be there for long - just a few more weeks.
We need a flyer to promote locally our pop up shop (temporary shop) with a Clearance Sale. The flyer will be sent by post or by hand to the local residents and by email to ex customers that bought from us before and we have their email address...
We need a modern fresh design flyer. At the next stage we will provide text for each item (brief description, dimensions and price) so allow some space for this.
Maybe we need to add a message or something to make people want to come quickly? For example most of the items are ex display or the last item and if they want it they should hurry as one is gone its gone. or you may have a better suggestion - let me know.
if you want to see some ideas of our website then 7QK.co.uk

Target Market(s)

Local Residents around shop

Industry/Entity Type

Retail

Colors
0255a3
3176b5
85abd2

Requirements
Must have
• price tag showing RRP or WAS price and the Clearance Sale price
• Opening Hours: Mon-Fri 9:00am - 5:00pm, Sat: 9:00am - 4:00pm, Sun: Closed
• Tel: 0208 915 2730
• Shop Address: 184 Birch Rowe, Elmwick Vale, London, N21 7PD
Nice to have
• Parking behind Bo Tarvins
• Map of location

```html
<!DOCTYPE html>
<html lang="en">
<head>
<meta charset="utf-8">
<title>7QK Furniture – Pop Up Shop Clearance Flyer</title>
<link rel="stylesheet" href="https://fonts.googleapis.com/css2?family=Open+Sans:wght@300;400;600;700&family=Oswald:wght@600&display=swap">
<style>
  :root{
    --navy:#233e7f;
    --royal:#2a5eb0;
    --frame:#2455b0;
    --sky:#1c9be0;
    --ink:#333;
    --muted:#777;
    --sale:#0255a3;
    --paper:#ffffff;
    --backdrop:#2b2c27;
  }
  *{box-sizing:border-box;margin:0;padding:0}
  html,body{width:1200px;height:1200px;overflow:hidden;background:var(--backdrop)}
  body{position:relative;font-family:"Open Sans",sans-serif;color:var(--ink)}
  .flyer{position:absolute;left:200px;top:35px;width:800px;height:1130px;background:var(--paper);overflow:hidden}
  .hero{position:absolute;left:0;top:0;width:800px;height:310px}
  .hero-photo{position:absolute;inset:0;background:linear-gradient(180deg,#f4f5f7 0%,#d9dde2 30%,#7d8590 55%,#6f747b 72%,#9a6a44 88%,#b07a4c 100%)}
  .hero-wave{position:absolute;left:0;top:0;width:800px;height:310px}
  .brand{position:absolute;left:0;right:0;top:14px;text-align:center}
  .brand-name{display:inline-flex;align-items:center;gap:14px;font-weight:300;font-size:40px;color:#1f2226;letter-spacing:.5px;text-transform:uppercase;line-height:1}
  .brand-mark{width:26px;height:26px;background:var(--royal)}
  .brand-tag{font-weight:700;font-size:16px;color:#1f2226;margin-top:8px;margin-left:40px}
  .headline{position:absolute;left:0;right:0;top:292px;text-align:center;font-family:"Oswald",sans-serif;font-weight:600;color:var(--navy);font-size:50px;line-height:58px;letter-spacing:-.5px}
  .headline-rule{position:absolute;left:84px;top:411px;width:637px;height:4px;background:var(--sky)}
  .product{position:absolute;left:25px;width:225px;height:180px;background:var(--frame);padding:9px}
  .product-inner{width:100%;height:100%;background:var(--sky);padding:7px}
  .product-photo{width:100%;height:100%}
  .product-text{position:absolute;left:270px;width:185px;font-size:12.5px;line-height:17.6px}
  .product-text .spec{display:block;margin-top:9px;font-size:14px}
  .product-text .was{color:var(--muted);text-decoration:line-through}
  .product-text .now{font-weight:700;color:var(--sale)}
  .about-tab{position:absolute;left:557px;top:437px;width:193px;height:38px;background:var(--royal);border-radius:24px 24px 0 0;color:#fff;font-weight:700;font-size:27px;text-align:center;line-height:40px}
  .about-panel{position:absolute;left:505px;top:471px;width:295px;height:599px;background:var(--sky)}
  .about-copy{position:absolute;left:530px;top:486px;width:255px;color:#fff;font-size:12.8px;line-height:17.8px}
  .about-copy strong{font-weight:700}
  .about-copy .hours{margin-top:6px}
  .side-photo{position:absolute;left:524px;width:276px;height:146px}
  .offer{position:absolute;left:530px;top:1020px;width:250px;height:33px;border-radius:17px;background:var(--royal);color:#fff;font-weight:700;font-size:21px;text-align:center;line-height:33px}
  .footer{position:absolute;left:0;top:1070px;width:800px;height:60px;background:var(--royal);color:#fff;font-weight:700;font-size:13px}
  .contact{position:absolute;display:flex;align-items:center;gap:10px;top:0;height:60px}
  .contact svg{width:24px;height:24px;flex:none}
</style>
</head>
<body>
<main class="flyer">
  <header class="hero">
    <div class="hero-photo" role="img" aria-label="Living room with two grey leather sofas, yellow cushions and glass coffee tables"></div>
    <svg class="hero-wave" viewBox="0 0 800 310" preserveAspectRatio="none" aria-hidden="true">
      <path d="M0 300 L385 243 L760 292 L800 274 L800 310 L0 310 Z" fill="#ffffff"/>
      <path d="M0 300 L385 243 L760 292 L800 274 L800 283 L760 300 L385 252 L0 310 Z" fill="#2455b0"/>
    </svg>
    <div class="brand">
      <div class="brand-name"><span class="brand-mark"></span>7QK Furniture</div>
      <div class="brand-tag">POP UP SHOP CLEARANCE SALE</div>
    </div>
  </header>

  <h1 class="headline">Come &amp; grab the oppurtunity<br>to take these furnitures with You !</h1>
  <div class="headline-rule"></div>

  <section class="product" style="top:460px">
    <div class="product-inner"><div class="product-photo" role="img" aria-label="Wooden dining table with two chairs" style="background:linear-gradient(135deg,#fff 0%,#f3e6d6 45%,#c99560 60%,#fff 100%)"></div></div>
  </section>
  <div class="product-text" style="top:470px">
    Lorem ipsum dolor sit amet, consectetur adipiscing elit, sed do eiusmod tempor incididunt ut labore et dolore magna aliqua.
    <span class="spec">Dimension - 15x2x3 cm</span>
    <span class="spec">Was <span class="was">$ 12,000</span> &nbsp;Now <span class="now">$ 10,000</span></span>
  </div>

  <section class="product" style="top:660px">
    <div class="product-inner"><div class="product-photo" role="img" aria-label="Grey upholstered divan bed in a bedroom" style="background:linear-gradient(160deg,#a8adb3 0%,#e8ecef 45%,#f4f4f2 60%,#6d6f73 100%)"></div></div>
  </section>
  <div class="product-text" style="top:672px">
    Lorem ipsum dolor sit amet, consectetur adipiscing elit, sed do eiusmod tempor incididunt ut labore et dolore magna aliqua.
    <span class="spec" style="margin-top:15px">Dimension - 15x2x3 cm</span>
    <span class="spec" style="margin-top:14px">Was <span class="was">$ 12,000</span> &nbsp;Now <span class="now">$ 10,000</span></span>
  </div>

  <section class="product" style="top:868px">
    <div class="product-inner"><div class="product-photo" role="img" aria-label="Round white dining table with grey chairs" style="background:linear-gradient(180deg,#d6d8da 0%,#f0f1f2 40%,#ffffff 60%,#5e6166 100%)"></div></div>
  </section>
  <div class="product-text" style="top:882px">
    Lorem ipsum dolor sit amet, consectetur adipiscing elit, sed do eiusmod tempor incididunt ut labore et dolore magna aliqua.
    <span class="spec" style="margin-top:15px">Dimension - 15x2x3 cm</span>
    <span class="spec" style="margin-top:8px">Was <span class="was">$ 12,000</span> &nbsp;Now <span class="now">$ 10,000</span></span>
  </div>

  <div class="about-panel"></div>
  <h2 class="about-tab">About Us</h2>
  <div class="about-copy">
    <p>Our pop up shop is open for a few more weeks only. Most items are ex display or the last one left – once it's gone, it's gone!</p>
    <p class="hours"><strong>Opening Hours</strong><br>Mon-Fri: 9:00am - 5:00pm<br>Sat: 9:00am - 4:00pm &nbsp;|&nbsp; Sun: Closed<br>Parking behind Bo Tarvins</p>
  </div>
  <div class="side-photo" style="top:682px;background:linear-gradient(180deg,#e9ecee 0%,#cfd6d6 40%,#b59a86 65%,#a33b45 80%,#d9d2c8 100%)" role="img" aria-label="Bedroom with wooden bed and red throw"></div>
  <div class="side-photo" style="top:846px;background:linear-gradient(180deg,#e6e8ea 0%,#bfc4c9 35%,#4e5564 60%,#3c4250 75%,#e8e8e6 100%)" role="img" aria-label="Dark grey sofa bed with blue throw"></div>
  <div class="offer">One Time Offer Only !</div>

  <footer class="footer">
    <div class="contact" style="left:45px">
      <svg viewBox="0 0 24 24" fill="none" stroke="#fff" stroke-width="1.8" aria-hidden="true"><path d="M6 3l3 4-2 2c1 3 4 6 7 7l2-2 4 3-2 3C10 20 4 14 3 5z"/></svg>
      <span>Tel: 0208 915 2730</span>
    </div>
    <div class="contact" style="left:306px">
      <svg viewBox="0 0 24 24" fill="none" stroke="#fff" stroke-width="1.8" aria-hidden="true"><circle cx="12" cy="12" r="9.5"/><path d="M2.5 12h19M12 2.5c3 3 3 16 0 19M12 2.5c-3 3-3 16 0 19"/></svg>
      <span>7QK.co.uk</span>
    </div>
    <div class="contact" style="left:518px">
      <svg viewBox="0 0 24 24" fill="none" stroke="#fff" stroke-width="1.8" aria-hidden="true"><path d="M12 21s-6-6.5-6-11a6 6 0 0112 0c0 4.5-6 11-6 11z"/><circle cx="12" cy="10" r="2.3"/><path d="M5 21h14"/></svg>
      <span>184 Birch Rowe, Elmwick Vale,<br>London, N21 7PD</span>
    </div>
  </footer>
</main>
</body>
</html>
```